Meridale Eating needs Stationary and a business card

We would like to use our current logo. The text can be moved around as needed. The stationary needs to be a 'first page' where the logo is more prominent to be impressive on higher quality paper and a second page where the logo is more subtle where there will be much more information on the page. There are 2 clinic locations which will need include name, address, phone number, fax number, web address. The business card should be single sided and contain this information also.
The design must be contemporary and sophisticated as this is a science based diet run out of a medical clinic.

Target Market(s)

People wanting to lose weight, athletes looking to optimise performance, people with arthritis or fighting cancer

Industry/Entity Type

Business

Contact Information for Business Card

must use the logo. I have attached an example card with the practice details on it. there must be space for the doctors name. Also the website www.meridaleeating.example.au

Requirements
Must have
• the logo, the business adresses and phone numbers, the website, the doctors name and qualifications
Nice to have
• some creativity
Should not have
• Do not simply reproduce the existing card please

```html
<!DOCTYPE html>
<html lang="en">
<head>
<meta charset="utf-8">
<title>Meridale Eating – Stationery</title>
<link rel="stylesheet" href="https://fonts.googleapis.com/css2?family=Jost:wght@400;500;600&display=swap">
<style>
  :root {
    --backdrop: #e6e7e9;
    --paper: #ffffff;
    --navy: #346a9a;
    --brand-blue: #2e6aa8;
    --sky: #38c4f0;
    --text-grey: #7a7d80;
    --faint-fill: #eef4fb;
    --faint-ring: #e3ebf3;
  }
  * { margin: 0; padding: 0; box-sizing: border-box; }
  html, body { width: 1200px; height: 790px; overflow: hidden; background: var(--backdrop); }
  body { position: relative; font-family: "Jost", "Futura", sans-serif; }

  .sheet {
    position: absolute; top: 70px; width: 502px; height: 650px;
    box-shadow: 4px 5px 7px rgba(0,0,0,.35); overflow: hidden;
  }
  .letterhead { left: 76px; background: var(--paper); }
  .cover { left: 622px; background: var(--navy); }

  .sheet-art { position: absolute; inset: 0; width: 502px; height: 650px; }

  .brand { position: absolute; left: 20px; top: 16px; display: flex; align-items: center; gap: 14px; }
  .brand-dot { width: 54px; height: 54px; border-radius: 50%; background: var(--sky); }
  .brand-name { color: var(--brand-blue); font-weight: 600; font-size: 20px; letter-spacing: .3px; }

  .clinic {
    position: absolute; top: 20px; font-size: 10.5px; line-height: 12px; color: var(--text-grey);
  }
  .clinic-name { color: var(--brand-blue); font-weight: 500; }
  .clinic-label { color: var(--brand-blue); }
  .clinic-halden { left: 285px; }
  .clinic-corvale { left: 390px; padding-left: 7px; border-left: 1.5px solid var(--brand-blue); }

  .footer-links {
    position: absolute; left: 32px; top: 617px; display: flex;
    color: #fff; font-size: 10px; line-height: 12px;
  }
  .footer-links .link { padding: 0 7px; text-align: center; }
  .footer-links .link + .link { border-left: 1px solid #fff; text-align: left; }
  .footer-links .link:first-child { padding-left: 0; }

  .cover-name {
    position: absolute; left: 0; right: 0; top: 508px; text-align: center;
    color: #fff; font-weight: 500; font-size: 40px; letter-spacing: .5px;
  }
</style>
</head>
<body>

  <section class="sheet letterhead">
    <svg class="sheet-art" viewBox="0 0 502 650" aria-hidden="true">
      <circle class="watermark" cx="398" cy="546" r="78" fill="var(--faint-fill)" stroke="var(--faint-ring)" stroke-width="4"/>
      <path class="wave-accent" d="M0 606 C 90 578, 190 592, 280 612 C 360 630, 440 632, 502 618" fill="none" stroke="var(--sky)" stroke-width="4"/>
      <path class="wave-band" d="M0 612 C 90 588, 190 600, 280 620 C 360 636, 440 636, 502 624 L502 650 L0 650 Z" fill="var(--navy)"/>
    </svg>

    <div class="brand">
      <span class="brand-dot"></span>
      <span class="brand-name">MERIDALE EATING</span>
    </div>

    <div class="clinic clinic-halden">
      <div class="clinic-name">Halden</div>
      <div>47-49 Larchmont Road</div>
      <div>Halden NSW 2199</div>
      <div><span class="clinic-label">T:</span> 02 9000 1234</div>
    </div>
    <div class="clinic clinic-corvale">
      <div class="clinic-name">Corvale</div>
      <div>160 Ashby Road</div>
      <div>Corvale NSW 2098</div>
      <div><span class="clinic-label">F:</span> 02 9000 5678</div>
    </div>

    <div class="footer-links">
      <div class="link">Shoulder and Elbow<br>www.halvorsen.example.au</div>
      <div class="link">Knee Surgery<br>www.kneeclinic.example.au</div>
    </div>
  </section>

  <section class="sheet cover">
    <svg class="sheet-art" viewBox="0 0 502 650" aria-hidden="true">
      <circle class="cover-dot" cx="250" cy="266" r="104" fill="var(--sky)"/>
      <path class="wave-line" d="M0 614 C 120 638, 250 610, 360 594 C 430 584, 480 590, 502 598" fill="none" stroke="#fff" stroke-width="4"/>
      <path class="wave-band" d="M0 622 C 120 644, 250 618, 360 602 C 430 592, 480 598, 502 606 L502 650 L0 650 Z" fill="var(--sky)"/>
    </svg>
    <div class="cover-name">MERIDALE EATING</div>
  </section>

</body>
</html>
```